Power point design for a financial seminar

I would like to receive 10 designed power point slides with the same look & feel that should related to finance since its for a seminar related to stock markets and economics. Please note that texts are in Hebrew (translate is attached in a Word document).
There should be background with upper and bottom layers similar to all to include the attached logo.
All slides should have a Title and some of the slides should have designed bullets and other generic graphic elements that we will use in our presentation.
Please note that text should be right to left so texts will be aligned to the right and graphics at the left/upper/bottom
Youngsters

```html
<!DOCTYPE html>
<html lang="he" dir="rtl">
<head>
<meta charset="utf-8">
<title>קורס שוק ההון – בסיס</title>
<link href="https://fonts.googleapis.com/css2?family=Heebo:wght@400;500;700;800&display=swap" rel="stylesheet">
<style>
:root{
  --blue-deep:#0c3d86;
  --blue:#1a5cb2;
  --blue-mid:#2f78cf;
  --blue-light:#dbe9f8;
  --blue-pale:#eef5fc;
  --teal:#2cc3a6;
  --teal-dark:#1aa88f;
  --ink:#2b3440;
  --muted:#6b7684;
  --line:#d9e1ea;
  --paper:#ffffff;
  --stage:#eef1f5;
}
*{box-sizing:border-box;margin:0;padding:0}
html,body{width:720px;height:1200px;overflow:hidden}
body{background:var(--stage);font-family:'Heebo',sans-serif;color:var(--ink);position:relative}

.slide{position:absolute;background:var(--paper);overflow:hidden;box-shadow:0 10px 26px rgba(20,50,90,.18)}
.slide--small{width:315px;height:177px}

/* title slide */
.slide--title{left:40px;top:70px;width:640px;height:360px;background:linear-gradient(180deg,var(--blue-mid) 0%,var(--blue) 55%,var(--blue-deep) 100%)}
.title-photo{position:absolute;inset:0;background:linear-gradient(160deg,rgba(255,255,255,.12) 0%,rgba(255,255,255,0) 45%,rgba(8,40,90,.35) 100%)}
.title-logo-tab{position:absolute;left:50%;top:0;transform:translateX(-50%);width:190px;height:96px;background:var(--blue-pale);border-radius:0 0 14px 14px;display:flex;flex-direction:column;align-items:center;justify-content:center;gap:4px}
.brand-mark{border-radius:50%;background:var(--teal)}
.title-logo-tab .brand-mark{width:30px;height:30px}
.brand-name{color:var(--blue-deep);font-weight:700;line-height:1.1;text-align:center}
.title-logo-tab .brand-name{font-size:14px}
.title-heading{position:absolute;top:150px;left:0;right:0;text-align:center;color:#fff;font-size:40px;font-weight:800;letter-spacing:.5px}
.title-presenter{position:absolute;top:230px;left:50%;transform:translateX(-50%);width:220px;height:44px;border-radius:22px;background:linear-gradient(90deg,var(--teal-dark),var(--teal));color:#fff;font-size:20px;font-weight:500;display:flex;align-items:center;justify-content:center}

/* shared small slide chrome */
.slide-head{position:absolute;top:0;left:0;right:0;height:28px;background:linear-gradient(90deg,#fff 0%,var(--blue-pale) 60%,var(--blue-light) 100%)}
.slide-head::after{content:"";position:absolute;left:0;right:0;bottom:0;height:2px;background:linear-gradient(90deg,transparent,var(--blue-mid))}
.slide-title{position:absolute;top:6px;right:12px;font-size:11px;font-weight:800;color:var(--blue)}
.mini-brand{position:absolute;top:5px;left:9px;display:flex;align-items:center;gap:3px}
.mini-brand .brand-mark{width:9px;height:9px}
.mini-brand .brand-name{font-size:5px}
.page-corner{position:absolute;left:0;bottom:0;width:20px;height:14px;background:var(--blue);border-top-right-radius:8px;color:#fff;font-size:6px;display:flex;align-items:center;justify-content:center}

/* grid positions */
.pos-a{left:40px;top:470px}
.pos-b{left:365px;top:470px}
.pos-c{left:40px;top:677px}
.pos-d{left:365px;top:677px}
.pos-e{left:40px;top:884px}
.pos-f{left:365px;top:884px}

/* lecturer background */
.lecturer-photo{position:absolute;left:0;top:28px;bottom:0;width:96px;background:linear-gradient(160deg,var(--blue-mid),var(--blue-deep))}
.credential-list{position:absolute;right:12px;left:110px;top:38px;list-style:none}
.credential-list li{display:flex;align-items:center;gap:6px;height:25px;border-bottom:1px solid var(--line);font-size:6.5px;color:var(--ink)}
.credential-icon{width:13px;height:13px;border-radius:50%;background:var(--blue-light);flex-shrink:0;display:flex;align-items:center;justify-content:center}
.credential-icon span{width:5px;height:5px;border-radius:1px;background:var(--blue-mid)}

/* exchange topics */
.exchange-photo{position:absolute;left:0;right:0;top:28px;height:34px;background:linear-gradient(90deg,var(--blue-deep),var(--blue-mid))}
.topic-grid{position:absolute;left:12px;right:12px;top:46px;display:grid;grid-template-columns:repeat(4,1fr);gap:8px 7px}
.topic-card{background:#fff;height:50px;box-shadow:0 2px 6px rgba(20,50,90,.15);padding:4px 5px;font-size:6px;line-height:1.3;color:var(--ink)}
.topic-num{display:block;color:var(--blue-light);font-size:8px;font-weight:800;text-align:left}

/* securities wheel */
.wheel{position:absolute;left:50%;top:34px;transform:translateX(-50%)}
.wheel-label{position:absolute;font-size:7.5px;font-weight:500;color:var(--ink)}
.wheel-label::after{content:"";display:block;height:1px;width:60px;background:var(--line);margin-top:3px}
.wheel-label--bottom::after{display:none}

/* investment route */
.route{position:absolute;left:10px;top:30px}
.route-label{position:absolute;font-size:7.5px;font-weight:500;color:var(--ink);white-space:nowrap}

/* derivatives */
.derivative-card{position:absolute;top:46px;width:118px;height:100px;border-radius:10px;overflow:hidden;background:linear-gradient(160deg,#9db9d9,var(--blue))}
.derivative-card span{position:absolute;bottom:10px;right:10px;color:#fff;font-size:10px;font-weight:700}

/* indices */
.index-row{position:absolute;right:12px;left:12px;height:46px;display:flex;align-items:center;gap:10px;border-bottom:1px solid var(--line)}
.index-flag{width:22px;height:22px;border-radius:4px;background:var(--blue);flex-shrink:0}
.index-flag--alt{background:var(--blue-light);border:2px solid var(--blue-mid)}
.index-text{font-size:7px;line-height:1.4;color:var(--ink)}
.index-text b{display:block;color:var(--blue);font-size:8px}
</style>
</head>
<body>

<section class="slide slide--title">
  <div class="title-photo" role="img" aria-label="תמונת רקע כחולה של גרף מסחר בבורסה"></div>
  <div class="title-logo-tab">
    <span class="brand-mark"></span>
    <span class="brand-name">מועדון הצמיחה<br>של דן לוינסון</span>
  </div>
  <h1 class="title-heading">קורס שוק ההון- בסיס (חדש)</h1>
  <div class="title-presenter">נועה לוינסון</div>
</section>

<section class="slide slide--small pos-a">
  <div class="slide-head"></div>
  <h2 class="slide-title">רקע על המרצה</h2>
  <div class="lecturer-photo" role="img" aria-label="תמונה כחולה של סביבת עבודה פיננסית"></div>
  <ul class="credential-list">
    <li><span class="credential-icon"><span></span></span>בעל שני תארים בתחום עסקים</li>
    <li><span class="credential-icon"><span></span></span>מרצה במכללת אופק</li>
    <li><span class="credential-icon"><span></span></span>יזם וניהל תיקי השקעות פרטיים</li>
    <li><span class="credential-icon"><span></span></span>כותב טורי דעה בנושאי כלכלה</li>
    <li><span class="credential-icon"><span></span></span>הקים וניהל חברה למסחר בנגזרים פיננסיים</li>
  </ul>
  <div class="page-corner">2</div>
</section>

<section class="slide slide--small pos-b">
  <div class="slide-head"></div>
  <h2 class="slide-title">בורסה</h2>
  <div class="mini-brand"><span class="brand-mark"></span><span class="brand-name">מועדון הצמיחה</span></div>
  <div class="exchange-photo" role="img" aria-label="תמונה כחולה של אולם מסחר"></div>
  <div class="topic-grid">
    <div class="topic-card"><span class="topic-num">01</span>מה זו בורסה?</div>
    <div class="topic-card"><span class="topic-num">02</span>ההיסטוריה של הבורסה</div>
    <div class="topic-card"><span class="topic-num">03</span>חברות ציבוריות והנפקות</div>
    <div class="topic-card"><span class="topic-num">04</span>בורסות מובילות בעולם</div>
    <div class="topic-card"><span class="topic-num">05</span>ההבדל בין שוק ראשוני לשוק משני</div>
    <div class="topic-card"><span class="topic-num">06</span>איך הבורסה משפיעה על הכלכלה</div>
    <div class="topic-card"><span class="topic-num">07</span>מי פועל בבורסה</div>
    <div class="topic-card"><span class="topic-num">08</span>שעות ושיטות המסחר</div>
  </div>
  <div class="page-corner">3</div>
</section>

<section class="slide slide--small pos-c">
  <div class="slide-head"></div>
  <h2 class="slide-title">ני"ע נסחרים בבורסה</h2>
  <div class="mini-brand"><span class="brand-mark"></span><span class="brand-name">מועדון הצמיחה</span></div>
  <svg class="wheel" width="120" height="120" viewBox="-65 -65 130 130" aria-hidden="true">
    <g stroke="#fff" stroke-width="3">
      <path d="M0 0 L0 -60 A60 60 0 0 1 57.06 -18.54Z" fill="#1a5cb2"/>
      <path d="M0 0 L57.06 -18.54 A60 60 0 0 1 35.27 48.54Z" fill="#2f78cf"/>
      <path d="M0 0 L35.27 48.54 A60 60 0 0 1 -35.27 48.54Z" fill="#0c3d86"/>
      <path d="M0 0 L-35.27 48.54 A60 60 0 0 1 -57.06 -18.54Z" fill="#2f78cf"/>
      <path d="M0 0 L-57.06 -18.54 A60 60 0 0 1 0 -60Z" fill="#1a5cb2"/>
    </g>
    <circle r="12" fill="#fff"/>
    <g fill="none" stroke="#fff" stroke-width="2" stroke-linecap="round">
      <path d="M20 -36 l6 -5 l4 3 l6 -7"/>
      <rect x="26" y="4" width="9" height="12" rx="1"/>
      <path d="M-4 36 l8 -8 M-4 28 l8 8 M0 26 v12"/>
      <rect x="-37" y="4" width="11" height="8" rx="1"/>
      <rect x="-32" y="-42" width="9" height="12" rx="1"/>
    </g>
  </svg>
  <span class="wheel-label" style="right:14px;top:40px">מניות</span>
  <span class="wheel-label" style="right:14px;top:100px">אג"חים</span>
  <span class="wheel-label" style="left:14px;top:40px">נגזרים פיננסים</span>
  <span class="wheel-label" style="left:14px;top:100px">קרנות נאמנות</span>
  <span class="wheel-label wheel-label--bottom" style="left:50%;transform:translateX(-50%);top:158px">תעודות סל</span>
  <div class="page-corner">4</div>
</section>

<section class="slide slide--small pos-d">
  <div class="slide-head"></div>
  <h2 class="slide-title">איך להשקיע</h2>
  <div class="mini-brand"><span class="brand-mark"></span><span class="brand-name">מועדון הצמיחה</span></div>
  <svg class="route" width="295" height="140" viewBox="0 0 295 140" aria-hidden="true">
    <path d="M20 90 C60 40 90 130 130 80 S200 40 240 60 S280 40 285 40" fill="none" stroke="#2cc3a6" stroke-width="4"/>
    <g fill="#1a5cb2">
      <rect x="34" y="56" width="26" height="26" rx="5" transform="rotate(45 47 69)"/>
      <rect x="103" y="75" width="26" height="26" rx="5" transform="rotate(45 116 88)"/>
      <rect x="173" y="47" width="26" height="26" rx="5" transform="rotate(45 186 60)"/>
      <rect x="238" y="37" width="26" height="26" rx="5" transform="rotate(45 251 50)"/>
    </g>
    <g fill="none" stroke="#fff" stroke-width="1.8" stroke-linecap="round">
      <path d="M44 63 v12 l-3 -3 M50 75 v-12 l3 3"/>
      <rect x="109" y="84" width="14" height="8" rx="1"/>
      <circle cx="186" cy="56" r="3"/><path d="M180 66 q6 -7 12 0"/>
      <path d="M244 54 h14 M245 54 v-6 M251 54 v-6 M257 54 v-6 M244 47 l7 -4 l7 4"/>
    </g>
  </svg>
  <span class="route-label" style="left:38px;top:40px">פקודות מסחר</span>
  <span class="route-label" style="left:110px;top:150px">סוגי עמלות</span>
  <span class="route-label" style="left:190px;top:44px">ברוקר</span>
  <span class="route-label" style="left:256px;top:112px">בנק</span>
  <div class="page-corner">5</div>
</section>

<section class="slide slide--small pos-e">
  <div class="slide-head"></div>
  <h2 class="slide-title">נגזרים פיננסיים</h2>
  <div class="mini-brand"><span class="brand-mark"></span><span class="brand-name">מועדון הצמיחה</span></div>
  <div class="derivative-card" style="right:30px" role="img" aria-label="תמונה כחולה של חתימה על חוזה"><span>חוזים עתידיים</span></div>
  <div class="derivative-card" style="left:30px" role="img" aria-label="תמונה כחולה של לחיצת ידיים עסקית"><span>אופציות</span></div>
  <div class="page-corner">6</div>
</section>

<section class="slide slide--small pos-f">
  <div class="slide-head"></div>
  <h2 class="slide-title">מדדים</h2>
  <div class="mini-brand"><span class="brand-mark"></span><span class="brand-name">מועדון הצמיחה</span></div>
  <div class="index-row" style="top:42px">
    <span class="index-flag"></span>
    <p class="index-text"><b>המדדים המובילים בארה"ב</b>מדדי המניות המובילים</p>
  </div>
  <div class="index-row" style="top:100px">
    <span class="index-flag index-flag--alt"></span>
    <p class="index-text"><b>המדדים המובילים בישראל</b>מדדי המניות המקומיים</p>
  </div>
  <div class="page-corner">7</div>
</section>

</body>
</html>
```